Redesign Website

I currently have a website www.kelvaromotionrx.com that I would like to have redesigned for esthetics and design limitations with the present platform. I will provide my logo, background logo (attached) , current site, foundation grip PSD.zip (attached) and a questionnaire (attached) from a web design company to provide the input to have an impressive site that pleases the eyes and makes an impact. I would also like the site to be mobile friendly.

IMPORTANT:
- The final PSD must include:
o Homepage Mockup
o Internal Pages Mockup
o Mobile site mockup
o Fonts files used in mockup

Final website will be responsive, using the Foundation Framework. Attached you will find a PSD of the Foundation grid – please use this and include with your final PSD. Here is a link for reference:
http://plimtex.com/article/1053/foundation-s-grid-and-photoshop-what-you-

Target Market(s)

Patients for physical therapy

Industry/Entity Type

It Company

Requirements
Must have
• Pages included in the present site. Photos and design should change.
Nice to have
• Should provide information necessary for patients to schedule an appointment
Should not have
• Should not be difficult to read.

```html
<!DOCTYPE html>
<html lang="en">
<head>
<meta charset="utf-8">
<title>Kelvaro Sports &amp; Orthopedic Physical Therapy</title>
<link href="https://fonts.googleapis.com/css2?family=Lora:ital,wght@0,700;1,700&family=Libre+Baskerville&family=Open+Sans:wght@400;600&display=swap" rel="stylesheet">
<style>
:root{
  --orange:#e8900f;
  --maroon:#7a1414;
  --red:#b5121b;
  --text:#333;
  --muted:#666;
  --light:#f1f2ee;
  --rule:#d6d6d6;
  --dark:#1e1e1c;
  --footer:#2b2b2b;
  --white:#fff;
}
*{margin:0;padding:0;box-sizing:border-box}
html,body{width:884px;height:1200px;overflow:hidden;background:var(--white)}
body{position:relative;font-family:"Open Sans",sans-serif;color:var(--text)}
.abs{position:absolute}
.heading{font-family:"Lora",serif;font-style:italic;font-weight:700;color:var(--maroon)}

/* header */
.site-header{left:0;top:0;width:884px;height:58px;background:var(--white);border-bottom:3px solid var(--orange)}
.brand{left:51px;top:0;width:139px;height:119px;background:var(--white);border:3px solid var(--orange);border-top:none;border-radius:0 0 6px 6px;z-index:3;display:flex;flex-direction:column;align-items:center;justify-content:center;gap:8px}
.brand-dot{width:34px;height:34px;border-radius:50%;background:var(--orange)}
.brand-name{font-family:"Lora",serif;font-weight:700;font-size:22px;color:var(--red)}
.main-nav{left:188px;top:27px;display:flex;font-family:"Libre Baskerville",serif;font-size:11.5px;text-transform:uppercase;letter-spacing:.2px}
.main-nav a{display:block;height:31px;line-height:31px;padding:0 13px;color:#333;text-decoration:none}
.main-nav a.active{background:var(--orange);color:var(--white);padding:0 14px}

/* hero */
.hero{left:0;top:58px;width:884px;height:353px;background:linear-gradient(180deg,#9cae6a 0%,#b9c77d 30%,#d9cfb4 60%,#efe4d4 100%)}
.hero-badge{left:55px;top:152px;width:226px;height:226px;border-radius:50%;background:rgba(255,255,255,.93);border:4px solid rgba(255,255,255,.7);box-shadow:0 2px 10px rgba(0,0,0,.15);overflow:hidden;text-align:center}
.hero-badge h1{font-family:"Lora",serif;font-style:italic;font-weight:700;color:var(--maroon);font-size:21px;line-height:23px;margin-top:30px}
.hero-badge p{font-size:10px;line-height:15.5px;color:var(--muted);margin:23px 12px 0}
.hero-badge .cta{position:absolute;left:0;bottom:0;width:100%;height:48px;background:var(--maroon);color:var(--white);font-family:"Lora",serif;font-style:italic;font-weight:700;font-size:12.5px;line-height:30px}

/* welcome */
.welcome{left:0;top:411px;width:884px;height:205px;background:var(--light)}
.doctor-photo{left:53px;top:27px;width:221px;height:178px;background:linear-gradient(180deg,#e2e2dc 0%,#d8b8a4 45%,#a9c4de 80%);border-radius:90px 90px 0 0}
.welcome h2{left:243px;top:32px;font-size:21px}
.welcome h3{left:243px;top:66px;font-family:"Libre Baskerville",serif;font-weight:400;font-size:13px;color:var(--orange)}
.welcome p{left:243px;top:94px;width:590px;font-size:10.5px;line-height:15.6px;color:#444}
.read-more{right:51px;top:180px;font-family:"Lora",serif;font-style:italic;font-weight:700;font-size:9.5px;color:var(--maroon)}

/* case studies & testimonials */
.section-title{display:flex;align-items:center;gap:12px;font-size:17.5px}
.section-title::after{content:"";flex:1;height:1px;background:var(--rule)}
.cases-title{left:51px;top:636px;width:423px}
.case-photo{top:668px;width:203px;height:151px}
.case-one{left:51px;background:linear-gradient(135deg,#cfd9e2,#e8d8c8 55%,#b9c49a)}
.case-two{left:271px;background:linear-gradient(135deg,#e6e6e6,#9c9c9c 60%,#5a5a5a)}
.testimonials{left:513px;top:636px;width:320px}
.testimonials .bar{display:flex;align-items:center;gap:10px}
.testimonials .bar .line{flex:1;height:1px;background:var(--rule)}
.testimonials .bar .label{font-size:17.5px}
.arrow-btn{width:13px;height:13px;border-radius:50%;background:#ddd;display:flex;align-items:center;justify-content:center}
.quote-box{left:520px;top:658px;width:306px;height:172px;border-left:1px solid var(--rule);border-right:1px solid var(--rule);border-bottom:1px solid var(--rule)}
.quote-box p{position:absolute;left:16px;top:6px;width:280px;font-size:10.3px;line-height:17.3px;color:#555}
.quote-box .mark{color:#bbb;font-family:"Lora",serif;font-weight:700}
.author-photo{left:14px;top:80px;width:72px;height:72px;border-radius:50%;background:linear-gradient(180deg,#e9e4e0,#d8b9a6 60%,#f3f3f3);border:3px solid #e2e2e2}
.author-name{left:96px;top:96px;font-size:12px}
.author-role{left:96px;top:119px;font-size:10.5px;color:#333}

/* feature band */
.feature-band{left:0;top:842px;width:884px;height:115px;background:linear-gradient(90deg,#262520,#3a3630 50%,#232220)}
.feature{top:0;width:196px;height:115px;text-align:center}
.feature svg{position:absolute;left:72px;top:20px}
.feature span{position:absolute;left:0;top:86px;width:100%;font-family:"Lora",serif;font-style:italic;font-weight:700;font-size:17px;color:var(--white)}
.feature.is-active span{color:var(--orange)}

/* location */
.location h2{left:50px;top:972px;font-size:14px}
.contact-row{left:50px;display:flex;align-items:flex-start;gap:8px;font-size:10.5px;line-height:13.5px;color:#555}
.followers{left:52px;top:1093px;display:flex;align-items:center;gap:6px}
.followers .label{font-size:14.5px;margin-right:6px}
.social{width:25px;height:25px;border-radius:50%;background:#ccc}
.social.first{background:#3b5c9a}
.map{left:309px;top:974px;width:522px;height:140px;background:linear-gradient(135deg,#e9e4dc,#dfe4d8 50%,#e7e1d6);border:4px solid var(--white);box-shadow:0 0 0 1px #e4e4e4}

/* footer */
.site-footer{left:0;top:1132px;width:884px;height:68px;background:var(--footer);text-align:center}
.footer-nav{margin-top:17px;font-size:10.3px;color:#bbb}
.footer-nav a{color:#ccc;text-decoration:none}
.footer-nav a.active{color:var(--orange)}
.footer-nav .sep{color:#666;margin:0 5px}
.copyright{margin-top:9px;font-size:10.3px;color:#bbb}
</style>
</head>
<body>

<header class="abs site-header"></header>
<div class="abs brand">
  <div class="brand-dot"></div>
  <div class="brand-name">Kelvaro</div>
</div>
<nav class="abs main-nav">
  <a class="active" href="#">Home</a>
  <a href="#">Mission Statement</a>
  <a href="#">Services</a>
  <a href="#">Insurance</a>
  <a href="#">New Patients</a>
  <a href="#">Contact Us</a>
</nav>

<section class="abs hero" role="img" aria-label="Photo of a young baseball player in a red helmet sliding into base on a dusty infield"></section>
<div class="abs hero-badge">
  <h1>Sports &amp;<br>orthopedic<br>physical therapy</h1>
  <p>Lorem ipsum dolor sit amet, consectetur adipiscing elit. Vivamus rutrum nibh elementum. malesuada.</p>
  <div class="cta">Find Location</div>
</div>

<section class="abs welcome">
  <div class="abs doctor-photo" role="img" aria-label="Portrait photo of the lead physical therapist in a light blue shirt"></div>
  <h2 class="abs heading">Welcome to Kelvaro !</h2>
  <h3 class="abs">Dr. Marten Oswell, PT, DPT, MS</h3>
  <p class="abs">Our services are the culmination of 15 years of experience of Dr. Marten Oswell, PT, DPT, MS in the sports and orthopedic physical therapy arena.&nbsp; Marten directed the rehabilitation services for the largest orthopedic group in Halden County. He has provided the services for an orthopedic and sports medicine group that had specialists in spine, shoulder, elbow, wrist, hand, hip, knee, ankle and foot surgery and treatment.&nbsp; His expertise is the treatment of any and all sports and orthopedic injuries, whether they are the result of trauma, repetitive movements or postures or the result of a surgical intervention.</p>
  <a class="abs read-more">Read more...</a>
</section>

<h2 class="abs heading section-title cases-title">Case Studies</h2>
<div class="abs case-photo case-one" role="img" aria-label="Photo of a clinician reviewing an x-ray with a patient"></div>
<div class="abs case-photo case-two" role="img" aria-label="Black and white photo of a therapist stretching a patient's leg"></div>

<div class="abs testimonials">
  <div class="bar">
    <span class="arrow-btn"><svg width="7" height="7" viewBox="0 0 7 7"><path d="M5 0.5 L2 3.5 L5 6.5" fill="none" stroke="#444" stroke-width="1.4"/></svg></span>
    <span class="line"></span>
    <span class="label heading">Testimonials</span>
    <span class="line"></span>
    <span class="arrow-btn"><svg width="7" height="7" viewBox="0 0 7 7"><path d="M2 0.5 L5 3.5 L2 6.5" fill="none" stroke="#444" stroke-width="1.4"/></svg></span>
  </div>
</div>
<div class="abs quote-box">
  <p><span class="mark">&ldquo;</span> Lorem ipsum dolor sit amet, consectetur adipiscing elit. Ut porta dolor at dolor varius, eu mollis lacus rutrum. Donec est nisl, ultrices vitae urna in, congue consequat felis. Aliquam ac nisi et felis auctor pulvina. <span class="mark">&rdquo;</span></p>
  <div class="abs author-photo" role="img" aria-label="Small round portrait of the reviewer"></div>
  <div class="abs heading author-name">Dr.Lorem ispum</div>
  <div class="abs author-role">Lorem ipsum dolor sit amet</div>
</div>

<section class="abs feature-band">
  <div class="abs feature is-active" style="left:51px">
    <svg width="52" height="56" viewBox="0 0 52 56">
      <path d="M26 2 C16 2 10 9 10 17 C10 27 26 42 26 42 C26 42 42 27 42 17 C42 9 36 2 26 2 Z" fill="var(--orange)"/>
      <circle cx="26" cy="17" r="6" fill="var(--dark)"/>
      <path d="M4 54 L12 36 L20 40 L26 36 L32 40 L40 36 L48 54 L32 50 L26 54 L20 50 Z" fill="none" stroke="var(--red)" stroke-width="3" stroke-linejoin="round"/>
    </svg>
    <span>Find Location</span>
  </div>
  <div class="abs feature" style="left:247px">
    <svg width="52" height="56" viewBox="0 0 52 56">
      <rect x="12" y="4" width="20" height="12" rx="2" fill="#ddd"/>
      <path d="M22 6 V14 M18 10 H26" stroke="#333" stroke-width="2"/>
      <circle cx="22" cy="24" r="8" fill="#ddd"/>
      <path d="M4 54 C4 40 12 34 22 34 C28 34 32 36 34 38 L34 54 Z" fill="#ddd"/>
      <circle cx="40" cy="44" r="10" fill="#ddd" stroke="#333" stroke-width="2"/>
      <path d="M40 38 V44 L44 46" stroke="#333" stroke-width="2" fill="none"/>
    </svg>
    <span>Appointment!</span>
  </div>
  <div class="abs feature" style="left:443px">
    <svg width="52" height="56" viewBox="0 0 52 56">
      <circle cx="26" cy="14" r="11" fill="#ddd"/>
      <path d="M6 54 C6 36 15 30 26 30 C37 30 46 36 46 54 Z" fill="#ddd"/>
      <path d="M18 32 C14 40 16 46 22 46 M34 32 C38 40 36 46 30 46" stroke="#333" stroke-width="2.5" fill="none"/>
      <circle cx="36" cy="46" r="3" fill="#333"/>
    </svg>
    <span>Services</span>
  </div>
  <div class="abs feature" style="left:638px">
    <svg width="52" height="56" viewBox="0 0 52 56">
      <g fill="#ccc">
        <circle cx="14" cy="10" r="5"/><circle cx="26" cy="8" r="5"/><circle cx="38" cy="10" r="5"/>
        <rect x="8" y="17" width="12" height="20" rx="3"/><rect x="20" y="15" width="12" height="22" rx="3"/><rect x="32" y="17" width="12" height="20" rx="3"/>
        <circle cx="8" cy="26" r="5"/><circle cx="20" cy="26" r="5"/><circle cx="32" cy="26" r="5"/><circle cx="44" cy="26" r="5"/>
        <rect x="2" y="32" width="12" height="22" rx="3"/><rect x="14" y="32" width="12" height="22" rx="3"/><rect x="26" y="32" width="12" height="22" rx="3"/><rect x="38" y="32" width="12" height="22" rx="3"/>
      </g>
    </svg>
    <span>Community</span>
  </div>
</section>

<section class="location">
  <h2 class="abs heading">Kelvaro Location!</h2>
  <div class="abs contact-row" style="top:998px">
    <svg width="20" height="22" viewBox="0 0 20 22"><path d="M10 1 C6 1 4 4 4 7 C4 11 10 16 10 16 C10 16 16 11 16 7 C16 4 14 1 10 1 Z" fill="none" stroke="#777" stroke-width="1.5"/><circle cx="10" cy="7" r="2" fill="#777"/><path d="M1 21 L4 15 L16 15 L19 21 Z" fill="none" stroke="#777" stroke-width="1.3"/></svg>
    <div>Kelvaro Sports &amp; Orthopedic Physical Therapy<br>218 Brookfield Avenue Suite 4</div>
  </div>
  <div class="abs contact-row" style="top:1039px">
    <svg width="20" height="18" viewBox="0 0 20 18"><path d="M4 2 L7 2 L8 6 L6 8 C7 10 9 12 11 13 L13 11 L17 12 L17 15 C17 16 16 17 15 17 C8 16 3 11 2 4 C2 3 3 2 4 2 Z" fill="#777"/></svg>
    <div>555-014-2290.</div>
  </div>
  <div class="abs contact-row" style="top:1067px">
    <svg width="20" height="16" viewBox="0 0 20 16"><rect x="1" y="2" width="18" height="12" fill="#777"/><path d="M1 2 L10 9 L19 2" fill="none" stroke="#fff" stroke-width="1.3"/></svg>
    <div>info@kelvaromotionrx.com</div>
  </div>
  <div class="abs followers">
    <span class="heading label">Follower</span>
    <span class="social first"></span>
    <span class="social"></span>
    <span class="social"></span>
    <span class="social"></span>
  </div>
  <div class="abs map" role="img" aria-label="Street map showing the clinic location with a red marker near a river"></div>
</section>

<footer class="abs site-footer">
  <nav class="footer-nav">
    <a class="active" href="#">Home</a><span class="sep">/</span><a href="#">Location</a><span class="sep">/</span><a href="#">Hours</a><span class="sep">/</span><a href="#">Our Story</a><span class="sep">/</span><a href="#">Mission Statement</a><span class="sep">/</span><a href="#">Services</a><span class="sep">/</span><a href="#">Insurance</a><span class="sep">/</span><a href="#">New Patients</a><span class="sep">/</span><a href="#">Contact Us</a><span class="sep">/</span><a href="#">Testimonials</a><span class="sep">/</span><a href="#">Community</a>
  </nav>
  <p class="copyright">Copyright © 2014.&nbsp; Kelvaro Sports &amp; Orthopedic Physical Therapy. All rights reserved.</p>
</footer>

</body>
</html>
```